High-end Investment firm website

It needs to feel very high-end. We like clean design which incorporates a good deal of white space with the use of imagery to be provided.

Here are a few examples of design which is appealing:
https://www.brindlecrestcapital.example
https://www.larkmoorgroup.example

Please use the following shade of blue in the design #7BAFD4.

Additional brand colors black, grey and white.

This quorvex doc has a link to all of the content for the site. It also has detailed design notes per section.

https://files.quorvexdocs.example/document/d/7TRQ2WpeLmnb8cvdKa3HJ0XsNf5ZgR1YtUoC9eV4qAs/edit?usp=sharing

Target Market(s)

Investors and companies in our target industries

Industry/Entity Type

Investment

Coding

Coded - Design and coding required

Number of Pages Required

5+ page

Font styles to use
Sans Serif

Requirements
Must have
• Clean feel, lots of white space.
Nice to have
• Clean graphics similar to https://www.brindlecrestcapital.example

```html
<!DOCTYPE html>
<html lang="en">
<head>
<meta charset="utf-8">
<title>Veyrant Holdings</title>
<link rel="stylesheet" href="https://fonts.googleapis.com/css2?family=Lato:wght@400;700&family=Ubuntu:wght@400;500&display=swap">
<style>
  :root {
    --brand-blue: #7BAFD4;
    --hero-blue: #3d77b5;
    --deep-blue: #2b5f95;
    --charcoal: #474747;
    --ink: #111111;
    --mist: #f1f2f2;
    --white: #ffffff;
    --orange: #f7a31c;
  }
  * { box-sizing: border-box; margin: 0; padding: 0; }
  html, body { width: 1200px; height: 4171px; overflow: hidden; }
  body { position: relative; background: var(--white); font-family: "Lato", sans-serif; color: var(--ink); }
  .abs { position: absolute; }
  .heading { font-family: "Ubuntu", sans-serif; font-weight: 400; }

  /* Header */
  .site-header { left: 0; top: 0; width: 1200px; height: 133px; background: var(--charcoal); }
  .brand-mark { display: flex; align-items: center; gap: 10px; font-family: "Lato", sans-serif; font-weight: 700; color: var(--brand-blue); letter-spacing: 2px; }
  .brand-mark .square { width: 14px; height: 14px; background: var(--brand-blue); }
  .site-header .brand-mark { left: 40px; top: 52px; font-size: 22px; }
  .main-nav { right: 52px; top: 52px; display: flex; gap: 37px; font-size: 20px; color: var(--white); }

  /* Hero */
  .hero-photo { left: 0; top: 133px; width: 583px; height: 487px; background: linear-gradient(180deg, #c7cfd6 0%, #98a4ae 45%, #7d8791 100%); }
  .hero-panel { left: 583px; top: 133px; width: 617px; height: 487px; background: var(--hero-blue); }
  .hero-title { left: 635px; top: 268px; font-size: 42px; line-height: 51px; color: var(--white); }

  /* Intro */
  .intro-title { left: 97px; top: 760px; font-size: 43px; color: var(--brand-blue); }
  .intro-lead { left: 97px; top: 808px; width: 535px; font-size: 26px; line-height: 32px; font-family: "Ubuntu", sans-serif; }
  .intro-note { left: 97px; top: 990px; width: 520px; font-size: 19px; line-height: 25px; }
  .intro-accent { left: 653px; top: 713px; width: 172px; height: 382px; background: var(--brand-blue); }
  .intro-photo { left: 688px; top: 770px; width: 409px; height: 272px; background: linear-gradient(135deg, #eef1f4 0%, #d9dee3 55%, #3a3d42 100%); }

  /* Focus */
  .focus-box { left: 89px; top: 1200px; width: 1016px; height: 299px; background: var(--mist); }
  .focus-title { left: 0; top: 1228px; width: 1194px; text-align: center; font-size: 32px; color: var(--brand-blue); }
  .focus-item { top: 1296px; width: 200px; text-align: center; font-size: 20px; line-height: 24px; color: #222; }
  .focus-item svg { display: block; margin: 0 auto 10px; }

  /* Capital */
  .capital-accent { left: 89px; top: 1641px; width: 169px; height: 277px; background: var(--deep-blue); }
  .capital-photo { left: 149px; top: 1673px; width: 539px; height: 209px; background: linear-gradient(90deg, #b08a60 0%, #d7c4a8 20%, #f3f4f6 40%, #e8edf2 100%); }
  .capital-title { left: 716px; top: 1678px; width: 400px; font-size: 33px; line-height: 38px; font-family: "Ubuntu", sans-serif; font-weight: 500; }
  .capital-note { left: 716px; top: 1813px; width: 370px; font-size: 15px; line-height: 18px; }

  /* Experience */
  .experience-band { left: 0; top: 2057px; width: 1200px; height: 579px; background: linear-gradient(135deg, #85b1dc 0%, #73a3d3 50%, #6d9dcf 100%); }
  .experience-title { left: 0; top: 2126px; width: 1200px; text-align: center; font-size: 43px; color: var(--white); }
  .experience-note { left: 0; top: 2198px; width: 1200px; text-align: center; font-size: 20px; line-height: 26px; color: var(--white); }
  .partner-name { width: 320px; text-align: center; font-family: "Lato", sans-serif; font-weight: 700; font-size: 30px; letter-spacing: 3px; color: var(--white); }

  /* Team */
  .team-brand { left: 0; top: 2716px; width: 1200px; justify-content: center; font-size: 24px; color: var(--deep-blue); }
  .team-title { left: 0; top: 2796px; width: 1200px; text-align: center; font-size: 32px; font-weight: 500; }
  .team-photo { top: 2877px; width: 256px; height: 256px; }
  .team-name { top: 3152px; width: 256px; text-align: center; font-size: 20px; }

  /* Contact */
  .contact-band { left: 0; top: 3352px; width: 1200px; height: 594px; background: linear-gradient(180deg, #2f5f93 0%, #2b5688 60%, #294f7e 100%); }
  .contact-brand { left: 162px; top: 3540px; font-size: 26px; color: var(--brand-blue); }
  .contact-title { left: 156px; top: 3602px; font-size: 62px; font-weight: 500; color: var(--white); }
  .contact-note { left: 160px; top: 3686px; font-size: 20px; line-height: 26px; color: var(--white); }
  .contact-cta { left: 160px; top: 3738px; font-size: 26px; font-weight: 700; color: var(--white); }
  .form-field { left: 614px; width: 470px; height: 58px; background: var(--white); padding-left: 26px; display: flex; align-items: center; font-size: 24px; color: #b5b5b5; font-family: "Lato", sans-serif; }
  .submit-btn { left: 617px; top: 3800px; width: 198px; height: 59px; background: var(--orange); color: var(--white); font-size: 31px; font-weight: 700; display: flex; align-items: center; justify-content: center; }

  /* Footer */
  .site-footer { left: 0; top: 3946px; width: 1200px; height: 225px; background: var(--charcoal); }
  .footer-col { top: 3976px; font-size: 20px; line-height: 25px; color: var(--white); }
  .footer-col .link { color: var(--brand-blue); font-weight: 700; }
  .footer-col .gap { height: 25px; }
  .footer-brand { left: 988px; top: 4060px; font-size: 24px; color: var(--brand-blue); }
</style>
</head>
<body>

<header class="abs site-header">
  <div class="abs brand-mark"><span class="square"></span>VEYRANT</div>
  <nav class="abs main-nav">
    <span>Home</span><span>About Us</span><span>Investment Focus</span><span>Industry Focus</span><span>Contact Us</span>
  </nav>
</header>

<section>
  <div class="abs hero-photo" role="img" aria-label="Aerial view of a city skyline with skyscrapers"></div>
  <div class="abs hero-panel"></div>
  <h1 class="abs heading hero-title">Partnering with<br>Exceptional Leaders<br>Building World-Class<br>Companies</h1>
</section>

<section>
  <h2 class="abs heading intro-title">Veyrant Holdings</h2>
  <p class="abs intro-lead">focuses on opportunities where it can support senior management to drive rapid growth and profit improvement through capital infusion, technology innovation and organizational expertise.</p>
  <p class="abs intro-note">We invest across a variety of growth industries with an emphasis on reshoring and rebuilding America.</p>
  <div class="abs intro-accent"></div>
  <div class="abs intro-photo" role="img" aria-label="Laptop screen showing financial charts"></div>
</section>

<section>
  <div class="abs focus-box"></div>
  <h2 class="abs heading focus-title">Areas of Focus</h2>

  <div class="abs focus-item" style="left:88px;">
    <svg width="80" height="80" viewBox="0 0 80 80" fill="none" stroke="#2b5f95" stroke-width="2.5">
      <path d="M24 36 V26 a16 16 0 0 1 32 0 V36" />
      <rect x="14" y="36" width="52" height="40" rx="6" fill="#bcd7ee"/>
      <circle cx="40" cy="55" r="7" fill="#7BAFD4"/>
    </svg>Defence
  </div>
  <div class="abs focus-item" style="left:287px;">
    <svg width="86" height="86" viewBox="0 0 86 86" fill="none" stroke="#2b5f95" stroke-width="2.5">
      <circle cx="40" cy="40" r="32" fill="#bcd7ee"/>
      <ellipse cx="40" cy="40" rx="14" ry="32"/>
      <path d="M8 40 H72 M14 24 H66 M14 56 H66 M40 8 V72"/>
      <path d="M54 54 L80 66 L68 70 L62 82 Z" fill="#7BAFD4"/>
    </svg>Cyber<br>Security
  </div>
  <div class="abs focus-item" style="left:478px;">
    <svg width="86" height="80" viewBox="0 0 86 80" fill="none" stroke="#2b5f95" stroke-width="2.5">
      <rect x="6" y="4" width="52" height="72" rx="4" fill="#bcd7ee"/>
      <path d="M6 14 H58"/>
      <path d="M32 24 C26 34 24 38 24 42 a8 8 0 0 0 16 0 C40 38 38 34 32 24 Z" fill="#7BAFD4"/>
      <path d="M46 76 L56 58 L66 76 Z M60 76 L70 58 L80 76 Z M53 58 L63 40 L73 58 Z" fill="#7BAFD4"/>
    </svg>Industrial
  </div>
  <div class="abs focus-item" style="left:671px;">
    <svg width="86" height="80" viewBox="0 0 86 80" fill="none" stroke="#2b5f95" stroke-width="2.5">
      <rect x="4" y="4" width="78" height="56" rx="3" fill="#bcd7ee"/>
      <path d="M43 60 V72 M26 76 H60"/>
      <circle cx="43" cy="24" r="8" fill="#7BAFD4"/>
      <path d="M27 48 a16 12 0 0 1 32 0 Z" fill="#7BAFD4"/>
    </svg>Digital<br>Enterprise
  </div>
  <div class="abs focus-item" style="left:875px;">
    <svg width="90" height="80" viewBox="0 0 90 80" fill="none" stroke="#2b5f95" stroke-width="2.5">
      <circle cx="24" cy="22" r="10" fill="#bcd7ee"/>
      <circle cx="66" cy="22" r="10" fill="#bcd7ee"/>
      <path d="M6 56 a18 16 0 0 1 36 0 Z M48 56 a18 16 0 0 1 36 0 Z" fill="#bcd7ee"/>
      <circle cx="45" cy="36" r="11" fill="#7BAFD4"/>
      <path d="M24 76 a21 18 0 0 1 42 0 Z" fill="#7BAFD4"/>
    </svg>Technology and<br>Professional Services
  </div>
</section>

<section>
  <div class="abs capital-accent"></div>
  <div class="abs capital-photo" role="img" aria-label="Printed bar and line charts on a wooden desk"></div>
  <h2 class="abs capital-title">We Place Capital For Long-Term Growth and Revenue Generation</h2>
  <p class="abs capital-note">Our investment horizon enables a focus on building strong sustainable companies, with empowered teams maximizing impact.</p>
</section>

<section>
  <div class="abs experience-band" role="img" aria-label="Faded photo of a business team at work, tinted blue"></div>
  <h2 class="abs heading experience-title">Investment Experience</h2>
  <p class="abs experience-note">The <strong>Veyrant Holdings</strong> team has invested in, managed and served<br>on the boards of a variety of high performing companies.</p>
  <div class="abs partner-name" style="left:55px; top:2390px;">NORTHVALE</div>
  <div class="abs partner-name" style="left:457px; top:2390px;">LARCHFIELD</div>
  <div class="abs partner-name" style="left:840px; top:2390px;">BRIGHTMERE ELECTRIC</div>
  <div class="abs partner-name" style="left:55px; top:2512px;">TELLURIX</div>
  <div class="abs partner-name" style="left:457px; top:2512px;">PINEWICK</div>
  <div class="abs partner-name" style="left:840px; top:2512px;">HARROWGATE TANKS</div>
</section>

<section>
  <div class="abs brand-mark team-brand"><span class="square"></span>VEYRANT</div>
  <h2 class="abs heading team-title">Management Team</h2>
  <div class="abs team-photo" style="left:30px; background:linear-gradient(180deg,#9aa4ad,#2c3140);" role="img" aria-label="Portrait of Elias in a dark suit"></div>
  <div class="abs team-photo" style="left:323px; background:linear-gradient(180deg,#4560a8,#1d2a55);" role="img" aria-label="Portrait of Rowan Hale on a blue backdrop"></div>
  <div class="abs team-photo" style="left:617px; background:linear-gradient(180deg,#ffffff 40%,#3b4150);" role="img" aria-label="Portrait of Tariq in a grey suit"></div>
  <div class="abs team-photo" style="left:903px; background:linear-gradient(180deg,#c9c4b8,#3a3530);" role="img" aria-label="Portrait of Mira in an office"></div>
  <div class="abs team-name" style="left:30px;">Elias</div>
  <div class="abs team-name" style="left:323px;">Rowan Hale</div>
  <div class="abs team-name" style="left:617px; top:3150px;">Tariq</div>
  <div class="abs team-name" style="left:903px;">Mira</div>
</section>

<section>
  <div class="abs contact-band" role="img" aria-label="Dusk city skyline tinted deep blue"></div>
  <div class="abs brand-mark contact-brand"><span class="square"></span>VEYRANT</div>
  <h2 class="abs heading contact-title">Contact Us</h2>
  <p class="abs contact-note">Interested in our services?<br>Have any questions?</p>
  <p class="abs contact-cta">Reach out to us now!</p>
  <div class="abs form-field" style="top:3457px;">Your Name</div>
  <div class="abs form-field" style="top:3526px;">Company Name</div>
  <div class="abs form-field" style="top:3595px;">Phone Number</div>
  <div class="abs form-field" style="top:3664px;">Email</div>
  <div class="abs form-field" style="top:3733px; width:473px;">How Can We Asist You?</div>
  <div class="abs submit-btn">Submit</div>
</section>

<footer class="abs site-footer"></footer>
<div class="abs footer-col" style="left:70px;">
  <div class="link">Home</div><div class="link">Contact Us</div>
</div>
<div class="abs footer-col" style="left:232px;">
  <div class="link">About Us</div><div>Elias</div><div>Tariq</div><div>Rowan</div><div>Cyrus</div><div>Mira</div>
</div>
<div class="abs footer-col" style="left:377px;">
  <div class="link">Investment Focus</div><div class="gap"></div><div class="link">Industry Focus</div><div>Our Investment</div>
</div>
<div class="abs brand-mark footer-brand"><span class="square"></span>VEYRANT</div>

</body>
</html>
```